Electrical Contracting Business card design

I would like a business card design for a new electrical business. I would like the print R.MOLT ELECTRICAL in large block lettering (spot gloss) on the front with atoms flying in a circle around the letter "A" of R.MOLT. Dark blue background, red lettering with the southern cross stars splashed in between the background and lettering.

On the rear of the card I would like the centre to have a box with 2 or 3 lines in it ( a space to write a time and date for the job to take place) surrounded by a big mass of confusing looking cables or a circuit diagram (something that would overwhelm people trying to make sense of it).

Thank you, I hope this isn't to detailed

Industry/Entity Type

Electrical

Contact Information for Business Card

R.MOLT ELECTRICAL
Phone: Brenn 0417853302
Brennr@mailvista.example
EC:47063

```html
<!DOCTYPE html>
<html lang="en">
<head>
<meta charset="utf-8">
<title>Job Card – Rear</title>
<link rel="stylesheet" href="https://fonts.googleapis.com/css2?family=Cabin:ital,wght@1,400&display=swap">
<style>
  :root {
    --navy: #1c1f55;
    --frame-red: #a51d22;
    --paper: #ffffff;
    --ink: #111111;
    --cable-black: #1e1e20;
    --cable-grey: #6b6d72;
    --cable-blue: #4a4fb0;
    --copper: #b5583a;
    --pale: #d9d8d6;
  }
  * { margin: 0; padding: 0; box-sizing: border-box; }
  html, body {
    width: 1200px;
    height: 741px;
    overflow: hidden;
    background: var(--paper);
  }
  .card-rear {
    position: relative;
    width: 1200px;
    height: 741px;
    overflow: hidden;
    background: var(--paper);
  }
  .side-band {
    position: absolute;
    left: 0;
    top: 0;
    width: 128px;
    height: 741px;
    background: var(--navy);
  }
  .cable-mass {
    position: absolute;
    left: 128px;
    top: 0;
    width: 1072px;
    height: 741px;
    background:
      radial-gradient(ellipse 220px 160px at 300px 80px, rgba(74, 79, 176, 0.85), transparent 70%),
      radial-gradient(ellipse 260px 140px at 560px 140px, rgba(107, 109, 114, 0.7), transparent 70%),
      radial-gradient(ellipse 200px 120px at 90px 120px, rgba(217, 216, 214, 0.8), transparent 70%),
      radial-gradient(ellipse 260px 200px at 900px 560px, rgba(181, 88, 58, 0.75), transparent 70%),
      radial-gradient(ellipse 220px 140px at 980px 700px, rgba(181, 88, 58, 0.6), transparent 70%),
      radial-gradient(ellipse 180px 120px at 200px 700px, rgba(217, 216, 214, 0.7), transparent 70%),
      linear-gradient(135deg, var(--cable-grey) 0%, var(--cable-black) 40%, #2b2b30 70%, var(--cable-black) 100%);
  }
  .job-box {
    position: absolute;
    left: 77px;
    top: 244px;
    width: 665px;
    height: 411px;
    background: var(--paper);
    border: 14px solid var(--frame-red);
  }
  .job-field {
    position: absolute;
    left: 35px;
    right: 38px;
    display: flex;
    align-items: baseline;
    font-family: "Cabin", "Gill Sans", sans-serif;
    font-style: italic;
    font-weight: 400;
    font-size: 22px;
    color: var(--ink);
  }
  .job-field .label { white-space: nowrap; padding-right: 4px; }
  .job-field .write-line {
    flex: 1;
    border-bottom: 1.3px solid var(--ink);
  }
  .field-time { top: 53px; }
  .field-date { top: 166px; }
  .field-job  { top: 279px; }
</style>
</head>
<body>
  <main class="card-rear">
    <div class="side-band"></div>
    <div class="cable-mass" role="img" aria-label="Close-up photograph of a tangled mass of black, grey, blue and copper electrical cables"></div>
    <section class="job-box">
      <div class="job-field field-time"><span class="label">time:</span><span class="write-line"></span></div>
      <div class="job-field field-date"><span class="label">date:</span><span class="write-line"></span></div>
      <div class="job-field field-job"><span class="label">job description:</span><span class="write-line"></span></div>
    </section>
  </main>
</body>
</html>
```